Business card revamp

we are refrigeration mechanic i need a modern professional double side business card using my current branding
The card information must have site address~ 17 Pellham st cobram, Vic 3644 postal address~ P.o. Box 862 cobram,Vic 3643 Phone Number~0358941637 Fax Nunber~0358936205 Email address~ brettk@vorlatek.com.au Title~ Manager Licence numbers~ AU47319, NSW 481927D Web site~ www.frostwaylane.com.au

```html
<!DOCTYPE html>
<html lang="en">
<head>
<meta charset="utf-8">
<title>Frostway Lane – Business Card</title>
<link href="https://fonts.googleapis.com/css2?family=Montserrat:wght@400;500;600;700&display=swap" rel="stylesheet">
<style>
  :root {
    --bg: #e9eaec;
    --card: #ffffff;
    --blue: #1b6fbd;
    --red: #c8202c;
    --ink: #2b2d33;
    --grey: #6d6f74;
    --rule: #8a8c90;
    --strand-blue: #a9c0e4;
    --strand-red: #e8b7a6;
  }
  * { box-sizing: border-box; margin: 0; padding: 0; }
  html, body { width: 1200px; height: 900px; overflow: hidden; }
  body {
    background: var(--bg);
    font-family: "Montserrat", sans-serif;
    color: var(--ink);
    position: relative;
  }
  .card {
    position: absolute;
    left: 250px;
    width: 700px;
    height: 400px;
    background: var(--card);
    box-shadow: 0 6px 18px rgba(0,0,0,0.12);
    overflow: hidden;
  }
  .card--front { top: 40px; }
  .card--back { top: 470px; }

  .strand {
    position: absolute;
    top: 0;
    width: 70px;
    height: 100%;
    background: linear-gradient(180deg, var(--strand-blue), var(--strand-red) 45%, var(--strand-blue));
    opacity: 0.55;
  }
  .card--front .strand { right: 40px; height: 340px; }
  .card--back .strand { left: 40px; }

  .brand { position: absolute; }
  .brand__name {
    font-weight: 700;
    color: var(--blue);
    text-transform: uppercase;
    letter-spacing: 1px;
    line-height: 1;
  }
  .brand__tag {
    font-size: 10px;
    font-weight: 500;
    letter-spacing: 1.5px;
    text-transform: uppercase;
    color: var(--grey);
    margin-top: 6px;
  }
  .card--front .brand { left: 40px; top: 50px; }
  .card--front .brand__name { font-size: 40px; }
  .card--back .brand { right: 50px; bottom: 70px; text-align: right; }
  .card--back .brand__name { font-size: 46px; }
  .card--back .brand__tag { font-size: 12px; }

  .person { position: absolute; left: 40px; top: 182px; width: 470px; }
  .person__name {
    font-size: 21px;
    font-weight: 600;
    letter-spacing: 1.5px;
    text-transform: uppercase;
    padding-bottom: 8px;
    border-bottom: 1px solid var(--rule);
  }
  .person__role {
    font-size: 16px;
    font-weight: 600;
    color: var(--red);
    text-transform: none;
    letter-spacing: 1px;
  }
  .licence {
    margin-top: 14px;
    font-size: 15px;
    letter-spacing: 2.5px;
  }
  .contacts { display: flex; margin-top: 16px; }
  .contacts__col { font-size: 16px; letter-spacing: 1px; }
  .contacts__col--phones { padding-right: 22px; border-right: 1px solid var(--rule); }
  .contacts__col--web { padding-left: 22px; }
  .contact { display: flex; align-items: center; gap: 8px; line-height: 1.45; }
  .contact svg { width: 16px; height: 16px; flex: none; }

  .address-band {
    position: absolute;
    left: 0; right: 0; bottom: 0;
    height: 40px;
    background: var(--blue);
    color: #fff;
    font-size: 15px;
    font-weight: 500;
    letter-spacing: 0.5px;
    padding-left: 40px;
    line-height: 40px;
  }
</style>
</head>
<body>

<section class="card card--front">
  <div class="strand" role="img" aria-label="Twisted red and blue ribbon decoration"></div>
  <div class="brand">
    <div class="brand__name">Frostway Lane</div>
    <div class="brand__tag">Heating and cooling specialists</div>
  </div>
  <div class="person">
    <div class="person__name">Brett Korvan <span class="person__role">/ Manager</span></div>
    <p class="licence">Licence numbers: AU47319, NSW 481927D</p>
    <div class="contacts">
      <div class="contacts__col contacts__col--phones">
        <div class="contact">
          <svg viewBox="0 0 16 16"><circle cx="8" cy="8" r="8" fill="var(--red)"/><path d="M4 7c0-2 8-2 8 0v1h-2V7H6v1H4z M5 9h6l1 3H4z" fill="#fff"/></svg>
          0358941637
        </div>
        <div class="contact">
          <svg viewBox="0 0 16 16"><circle cx="8" cy="8" r="8" fill="var(--red)"/><rect x="5" y="4" width="6" height="8" rx="1" fill="#fff"/><rect x="6" y="5" width="4" height="2" fill="var(--red)"/></svg>
          0358936205
        </div>
      </div>
      <div class="contacts__col contacts__col--web">
        <div class="contact">
          <svg viewBox="0 0 16 16"><circle cx="8" cy="8" r="8" fill="var(--red)"/><rect x="4" y="5" width="8" height="6" fill="#fff"/><path d="M4 5l4 3 4-3" stroke="var(--red)" fill="none"/></svg>
          brettk@vorlatek.com.au
        </div>
        <div class="contact">
          <svg viewBox="0 0 16 16"><circle cx="8" cy="8" r="8" fill="var(--red)"/><circle cx="8" cy="8" r="4.5" fill="none" stroke="#fff"/><path d="M3.5 8h9M8 3.5v9" stroke="#fff"/></svg>
          www.frostwaylane.com.au
        </div>
      </div>
    </div>
  </div>
  <div class="address-band">17 Pellham st Cobram, Vic 3644; P.o. Box 862 cobram,Vic 3643</div>
</section>

<section class="card card--back">
  <div class="strand" role="img" aria-label="Twisted red and blue ribbon decoration"></div>
  <div class="brand">
    <div class="brand__name">Frostway Lane</div>
    <div class="brand__tag">Heating and cooling specialists</div>
  </div>
</section>

</body>
</html>
```